Bref créative
Quang Loc Trading Co. Ltd
Business Card, Stationery (Letter head & Invoice)
Professional
Mrs. Lam Bich Ngoc
Director
218/45 Le Quy Don St. Dist 1, HoChiMinh city, Vietnam
quangloc@vkx.vn
Looking for a creative design which make the business card stand out from the rest.
I would like to be able to easily add additional information to my business cards and fill in some table in the letterhead so please make all the text file editable.
Please also include address of the company in the invoice and the letterhead.
Primary color: Red (Feel free to add secondary or third color which may be suitable)
Strong visibility of the company logo

```html
<!DOCTYPE html>
<html lang="en">
<head>
<meta charset="utf-8">
<title>Quang Loc Trading Co. Ltd — Business Card</title>
<link rel="stylesheet" href="https://fonts.googleapis.com/css2?family=Open+Sans:wght@400;600;700;800&display=swap">
<style>
  :root {
    --page-bg: #ece8e2;
    --card-bg: #ffffff;
    --brand-red: #b3121b;
    --brand-red-dark: #7a0a10;
    --swoosh-dark: #3a3a3a;
    --swoosh-light: #8a8a8a;
    --text-grey: #5a5a5a;
    --mark-grey: #d4d4d4;
    --faint-red: rgba(179, 18, 27, 0.06);
    --white: #ffffff;
  }
  * { box-sizing: border-box; margin: 0; padding: 0; }
  html, body {
    width: 1200px; height: 780px; overflow: hidden;
    background: var(--page-bg);
    font-family: "Open Sans", Arial, sans-serif;
  }
  .canvas { position: relative; width: 1200px; height: 780px; }
  .business-card {
    position: absolute; left: 100px; top: 90px;
    width: 1000px; height: 600px;
    background: var(--card-bg);
    border-radius: 36px;
    overflow: hidden;
    box-shadow: 0 14px 40px rgba(0,0,0,0.18);
  }
  .card-header-band { position: absolute; inset: 0; width: 1000px; height: 600px; }
  .holder { position: absolute; right: 42px; top: 26px; text-align: right; color: var(--white); }
  .holder-name { font-size: 30px; font-weight: 700; letter-spacing: 0.2px; }
  .holder-title { font-size: 19px; font-weight: 400; margin-top: 2px; }
  .brand-watermark {
    position: absolute; left: 560px; top: 220px;
    width: 300px; height: 300px; border-radius: 50%;
    background: var(--faint-red);
  }
  .brand-lockup {
    position: absolute; left: 40px; top: 250px;
    display: flex; align-items: center; gap: 22px;
  }
  .brand-dot {
    width: 96px; height: 96px; border-radius: 50%;
    background: var(--mark-grey);
  }
  .brand-name {
    font-size: 66px; font-weight: 800; color: var(--brand-red);
    letter-spacing: -1px; line-height: 1;
  }
  .address {
    position: absolute; left: 40px; top: 376px;
    font-size: 20px; line-height: 1.35; color: var(--text-grey);
  }
  .contact-list {
    position: absolute; left: 40px; top: 462px; list-style: none;
    font-size: 20px; color: var(--text-grey);
  }
  .contact-item { display: flex; align-items: center; gap: 12px; height: 34px; }
  .contact-icon { width: 20px; height: 20px; fill: var(--brand-red); flex: none; }
</style>
</head>
<body>
<div class="canvas">
  <article class="business-card">
    <svg class="card-header-band" viewBox="0 0 1000 600" aria-hidden="true">
      <defs>
        <linearGradient id="band-red" x1="0" y1="0" x2="0" y2="1">
          <stop offset="0" stop-color="var(--brand-red-dark)"/>
          <stop offset="0.55" stop-color="var(--brand-red)"/>
          <stop offset="1" stop-color="var(--brand-red-dark)"/>
        </linearGradient>
        <linearGradient id="band-swoosh" x1="0" y1="0" x2="1" y2="0">
          <stop offset="0" stop-color="var(--swoosh-dark)"/>
          <stop offset="1" stop-color="var(--swoosh-light)"/>
        </linearGradient>
      </defs>
      <path d="M0 0 H1000 V135 C720 115 380 120 0 185 Z" fill="url(#band-red)"/>
      <path d="M0 185 C380 120 720 115 1000 135 V143 C720 125 380 133 0 208 Z" fill="url(#band-swoosh)"/>
    </svg>

    <div class="holder">
      <div class="holder-name">Mrs. Lam Bich Ngoc</div>
      <div class="holder-title">Director</div>
    </div>

    <div class="brand-watermark" role="img" aria-label="Faint company mark"></div>

    <div class="brand-lockup">
      <div class="brand-dot"></div>
      <div class="brand-name">QUANG LOC</div>
    </div>

    <p class="address">218/45 Le Quy Don St. Dist 1<br>HoChiMinh city, Vietnam</p>

    <ul class="contact-list">
      <li class="contact-item">
        <svg class="contact-icon" viewBox="0 0 24 24" aria-hidden="true"><path d="M6.6 10.8a15.1 15.1 0 0 0 6.6 6.6l2.2-2.2c.3-.3.7-.4 1-.2 1.1.4 2.3.6 3.6.6.6 0 1 .4 1 1V20c0 .6-.4 1-1 1A17 17 0 0 1 3 4c0-.6.4-1 1-1h3.5c.6 0 1 .4 1 1 0 1.3.2 2.5.6 3.6.1.3 0 .7-.2 1z"/></svg>
        <span>(84.8) 3926514-3926520</span>
      </li>
      <li class="contact-item">
        <svg class="contact-icon" viewBox="0 0 24 24" aria-hidden="true"><path d="M7 1h10a2 2 0 0 1 2 2v18a2 2 0 0 1-2 2H7a2 2 0 0 1-2-2V3a2 2 0 0 1 2-2zm0 3v14h10V4zm5 15.5a1.2 1.2 0 1 0 0 2.4 1.2 1.2 0 0 0 0-2.4z"/></svg>
        <span>+84912457309</span>
      </li>
      <li class="contact-item">
        <svg class="contact-icon" viewBox="0 0 24 24" aria-hidden="true"><path d="M2 5h20v14H2zm2 2v.5l8 5 8-5V7zm0 2.8V17h16V9.8l-8 5z"/></svg>
        <span>quangloc@vkx.vn</span>
      </li>
    </ul>
  </article>
</div>
</body>
</html>
```